Fashion clothing business needs a label, swing tag and business card.

Independent womenswear label called "Tessa Wrenfold".
I'd like a design for a woven label to go on the clothes, a swing tag and business card design. The design should be simple, modern but timeless. Its a small business, made locally in Melbourne, Australia, produces quality garments for everyday wear using beautiful fabrics.

Target Market(s)

30+ ladies, who want quality everyday wear, who don't necessarily follow trends. They can be a bit edgy and willing to take a risk with something different.

Industry/Entity Type

Clothing

Font styles to use
Other font styles liked:
• I dont mind the typewriter font, but can it look modern? happy for you to choose.

Requirements
Should not have
• A difficult shape swing tag - as it might be more expensive for me to get printed and cut.

```html
<!DOCTYPE html>
<html lang="en">
<head>
<meta charset="utf-8">
<title>Tessa Wrenfold — Stationery &amp; Labels</title>
<link rel="stylesheet" href="https://fonts.googleapis.com/css2?family=Courgette&family=Arimo:wght@400&display=swap">
<style>
  :root {
    --paper: #ffffff;
    --ink: #1a1a1a;
    --ornament-dark: #111111;
    --ornament-light: rgba(17, 17, 17, 0.15);
    --backdrop: #e9e8e6;
    --edge: rgba(0, 0, 0, 0.12);
  }
  * { box-sizing: border-box; margin: 0; padding: 0; }
  html, body {
    width: 1200px;
    height: 900px;
    overflow: hidden;
    background: var(--backdrop);
  }
  .canvas {
    position: relative;
    width: 1200px;
    height: 900px;
    font-family: "Arimo", Arial, sans-serif;
    color: var(--ink);
  }
  .brand-name {
    font-family: "Courgette", cursive;
    font-weight: 400;
    color: var(--ink);
    white-space: nowrap;
  }

  /* Business card */
  .business-card {
    position: absolute;
    left: 60px;
    top: 70px;
    width: 560px;
    height: 320px;
    background: var(--paper);
    box-shadow: 0 1px 0 var(--edge), 0 6px 18px rgba(0,0,0,0.08);
  }
  .business-card .ornament {
    position: absolute;
    left: 0;
    top: 0;
    width: 150px;
    height: 100%;
    background: linear-gradient(90deg, var(--ornament-dark) 0%, var(--ornament-light) 100%);
  }
  .business-card .brand-name {
    position: absolute;
    left: 180px;
    top: 70px;
    font-size: 50px;
  }
  .business-card .contact {
    position: absolute;
    right: 36px;
    bottom: 40px;
    text-align: right;
    font-size: 17px;
    line-height: 1.55;
  }

  /* Swing tags */
  .swing-tags {
    position: absolute;
    left: 60px;
    top: 460px;
    display: flex;
    gap: 32px;
  }
  .swing-tag {
    position: relative;
    width: 170px;
    height: 380px;
    background: var(--paper);
    clip-path: polygon(0 13%, 22% 0, 78% 0, 100% 13%, 100% 86%, 70% 100%, 30% 100%, 0 86%);
  }
  .swing-tag .hole {
    position: absolute;
    left: 50%;
    top: 16px;
    width: 12px;
    height: 12px;
    margin-left: -6px;
    border-radius: 50%;
    background: var(--backdrop);
  }
  .swing-tag .brand-name {
    display: block;
    margin-top: 70px;
    text-align: center;
    font-size: 24px;
  }
  .swing-tag .tag-details {
    margin-top: 8px;
    text-align: center;
    font-size: 9.5px;
    line-height: 1.4;
  }
  .swing-tag .tag-fields {
    margin: 80px 0 0 20px;
    list-style: none;
    font-size: 14px;
    line-height: 2;
  }
  .swing-tag .ornament {
    position: absolute;
    left: 0;
    bottom: 0;
    width: 100%;
    height: 130px;
    background: linear-gradient(0deg, var(--ornament-dark) 0%, var(--ornament-light) 100%);
  }

  /* Woven label */
  .woven-label {
    position: absolute;
    left: 790px;
    top: 380px;
    width: 340px;
    height: 140px;
    background: var(--paper);
    box-shadow: 0 1px 0 var(--edge), 0 6px 18px rgba(0,0,0,0.08);
    display: flex;
    flex-direction: column;
    align-items: center;
    justify-content: center;
  }
  .woven-label .brand-name {
    font-size: 40px;
    line-height: 1.1;
  }
  .woven-label .origin {
    font-size: 16px;
    margin-top: 4px;
  }
</style>
</head>
<body>
<main class="canvas">

  <section class="business-card" aria-label="Business card">
    <div class="ornament" role="img" aria-label="Black floral swirl ornament"></div>
    <h1 class="brand-name">Tessa Wrenfold</h1>
    <p class="contact">mob: 0491570156<br>email: info@tessawrenfold.com</p>
  </section>

  <section class="swing-tags" aria-label="Swing tags">
    <article class="swing-tag">
      <span class="hole"></span>
      <span class="brand-name">Tessa Wrenfold</span>
      <p class="tag-details">Made in Australia<br>email: info@tessawrenfold.com</p>
      <div class="ornament" role="img" aria-label="Black floral swirl ornament"></div>
    </article>
    <article class="swing-tag">
      <span class="hole"></span>
      <ul class="tag-fields">
        <li>Size...........</li>
        <li>Style..........</li>
        <li>Price........</li>
      </ul>
      <div class="ornament" role="img" aria-label="Black floral swirl ornament"></div>
    </article>
    <article class="swing-tag">
      <span class="hole"></span>
      <span class="brand-name">Tessa Wrenfold</span>
      <p class="tag-details">Made in Australia<br>email: info@tessawrenfold.com</p>
      <div class="ornament" role="img" aria-label="Black floral swirl ornament"></div>
    </article>
  </section>

  <section class="woven-label" aria-label="Woven garment label">
    <span class="brand-name">Tessa Wrenfold</span>
    <span class="origin">Made in Australia</span>
  </section>

</main>
</body>
</html>
```